Tovalune letterhand

We are the new company dealing with care work.....We need a letter head although we don't have a logo...for the start we need the letterhead
Thanks

Industry/Entity Type

It Company

```html
<!DOCTYPE html>
<html lang="en">
<head>
<meta charset="utf-8">
<title>Tovalune Letterhead</title>
<link rel="stylesheet" href="https://fonts.googleapis.com/css2?family=Montserrat:wght@400&display=swap">
<style>
  :root {
    --backdrop: #686868;
    --paper: #f8f8f8;
    --brand-blue: #1a86c8;
    --ink: #444444;
    --ink-soft: #3d3d3d;
    --ghost: #ececec;
  }
  * { margin: 0; padding: 0; box-sizing: border-box; }
  html, body {
    width: 997px;
    height: 1200px;
    overflow: hidden;
    background: var(--backdrop);
  }
  .canvas {
    position: relative;
    width: 997px;
    height: 1200px;
    background: var(--backdrop);
    font-family: "Montserrat", sans-serif;
  }
  .letterhead {
    position: absolute;
    left: 187px;
    top: 159px;
    width: 622px;
    height: 881px;
    background: var(--paper);
  }
  .brand {
    position: absolute;
    left: 40px;
    top: 54px;
    width: 134px;
    text-align: center;
  }
  .brand-dot {
    display: block;
    width: 51px;
    height: 51px;
    margin: 0 auto 8px;
    border: 1.6px solid var(--brand-blue);
    border-radius: 50%;
  }
  .brand-name {
    font-size: 17.5px;
    font-weight: 400;
    letter-spacing: 4.2px;
    color: var(--ink-soft);
    text-transform: uppercase;
    white-space: nowrap;
  }
  .contact {
    position: absolute;
    left: 418px;
    top: 57px;
    list-style: none;
    font-size: 10.5px;
    line-height: 13.8px;
    color: var(--ink);
    white-space: nowrap;
  }
  .contact-item {
    display: flex;
    align-items: flex-start;
  }
  .contact-icon {
    width: 15px;
    flex: none;
    padding-top: 3px;
  }
  .contact-icon svg { display: block; fill: var(--brand-blue); }
  .watermark {
    position: absolute;
    left: 121px;
    top: 253px;
  }
</style>
</head>
<body>
<div class="canvas">
  <section class="letterhead">
    <header>
      <div class="brand">
        <span class="brand-dot"></span>
        <div class="brand-name">Tovalune</div>
      </div>
      <ul class="contact">
        <li class="contact-item">
          <span class="contact-icon"><svg width="7" height="6" viewBox="0 0 7 6"><path d="M0 2 Q3.5 -0.5 7 2 L6 3 L5 2.3 L2 2.3 L1 3 Z M1.5 3.2 H5.5 L6 6 H1 Z"/></svg></span>
          <span>00-418-907-2256</span>
        </li>
        <li class="contact-item">
          <span class="contact-icon"><svg width="7" height="7" viewBox="0 0 7 7"><circle cx="3.5" cy="3.5" r="3.2"/><path d="M0.5 3.5H6.5M3.5 0.5V6.5" stroke="#f8f8f8" stroke-width="0.6"/></svg></span>
          <span>www.tovalune.com</span>
        </li>
        <li class="contact-item">
          <span class="contact-icon"><svg width="7" height="5" viewBox="0 0 7 5"><rect width="7" height="5"/><path d="M0 0 L3.5 3 L7 0" fill="none" stroke="#f8f8f8" stroke-width="0.7"/></svg></span>
          <span>hello@tovalune.com</span>
        </li>
        <li class="contact-item">
          <span class="contact-icon"><svg width="6" height="8" viewBox="0 0 6 8"><path d="M3 8 C1 5 0 4 0 3 A3 3 0 0 1 6 3 C6 4 5 5 3 8 Z"/><circle cx="3" cy="3" r="1.1" fill="#f8f8f8"/></svg></span>
          <span>58 Fenwick Rd., Larkfield<br>Brindale, US 204871</span>
        </li>
      </ul>
    </header>
    <svg class="watermark" width="380" height="380" viewBox="0 0 380 380" aria-hidden="true">
      <circle cx="190" cy="190" r="181" fill="none" stroke="var(--ghost)" stroke-width="11"/>
    </svg>
  </section>
</div>
</body>
</html>
```